Stonelynk Business Card Design

The Stonelynk Co is an aggregate (crushing) equipment dealer serving Western Canadian provinces. Stonelynk is a distributor of aggregate equipment for different manufacturers.

We are looking to change and update the existing business card which has been used since the existence of the company. A copy of existing card has been attached for reference. The Stonelynk Co logo we want to remain the same and we want the green color to remain the same.

We are wanting something new with a different look. A refreshing card to show a new modern and updated look. No longer wanting to have the manufacturers on the back of the card but something more like our logo on the back of the card with a statement like "Crushing Solutions"

ideas could be:
- card can be different colors on front and back
- front or reverse of the card could possibly be the green color with the logo in black

Target Market(s)

Owners of Aggregate/Crushing companies

Requirements
Must have
• - logo to remain same along with same font within logo
• - green color to remain same
Nice to have
• as noted above under project description
Should not have

```html
<!DOCTYPE html>
<html lang="en">
<head>
<meta charset="utf-8">
<title>The Stonelynk Co – Business Card</title>
<link href="https://fonts.googleapis.com/css2?family=Oswald:wght@400;500;600;700&display=swap" rel="stylesheet">
<style>
  :root {
    --brand-green: #7a7d1e;
    --ink: #111111;
    --card-light: #e6e7e8;
    --card-dark: #050505;
    --backdrop: #ebe8e3;
    --white: #ffffff;
  }
  * { margin: 0; padding: 0; box-sizing: border-box; }
  html, body { width: 1200px; height: 800px; overflow: hidden; }
  body {
    background: var(--backdrop);
    font-family: "Oswald", "Arial Narrow", sans-serif;
    position: relative;
  }
  .card {
    position: absolute;
    top: 254px;
    width: 510px;
    height: 292px;
    overflow: hidden;
    box-shadow: 0 10px 24px rgba(0, 0, 0, 0.18);
  }

  /* Reverse */
  .card-back { left: 60px; background: var(--card-dark); }
  .back-mark {
    position: absolute;
    left: 205px; top: 56px;
    width: 100px; height: 100px;
    border-radius: 50%;
    background: var(--brand-green);
  }
  .back-name {
    position: absolute;
    left: 0; right: 0; top: 178px;
    text-align: center;
    color: var(--white);
    font-size: 26px;
    font-weight: 600;
    letter-spacing: 1px;
  }

  /* Front */
  .card-front { left: 630px; background: var(--card-light); color: var(--ink); }
  .front-mark {
    position: absolute;
    left: 26px; top: 24px;
    width: 34px; height: 34px;
    border-radius: 50%;
    background: var(--brand-green);
  }
  .company-name {
    position: absolute;
    right: 22px; top: 22px;
    font-size: 30px;
    font-weight: 600;
    letter-spacing: 0.5px;
    line-height: 1.2;
  }
  .tagline {
    position: absolute;
    right: 22px; top: 66px;
    font-size: 14px;
    font-weight: 500;
    color: var(--brand-green);
    letter-spacing: 0.4px;
  }
  .person-name {
    position: absolute;
    left: 28px; top: 86px;
    font-size: 22px;
    font-weight: 600;
    color: var(--brand-green);
    letter-spacing: 0.5px;
  }
  .person-title {
    position: absolute;
    left: 28px; top: 116px;
    font-size: 12px;
    font-weight: 500;
  }
  .rule {
    position: absolute;
    height: 2px;
    background: var(--ink);
  }
  .rule-top { left: 22px; right: 22px; top: 140px; }
  .rule-bottom { left: 198px; right: 22px; top: 204px; }
  .contact {
    position: absolute;
    font-size: 12px;
    font-weight: 400;
    line-height: 1.35;
    letter-spacing: 0.3px;
  }
  .contact-online { left: 28px; top: 148px; }
  .contact-office { left: 200px; top: 172px; }
  .contact-direct { right: 24px; top: 172px; text-align: right; }
  .contact-address { right: 24px; top: 212px; text-align: right; }
  .card-bands { position: absolute; left: 0; top: 0; }
</style>
</head>
<body>

  <section class="card card-back" aria-label="Business card reverse">
    <div class="back-mark"></div>
    <p class="back-name">THE STONELYNK CO.</p>
  </section>

  <section class="card card-front" aria-label="Business card front">
    <div class="front-mark"></div>
    <h1 class="company-name">THE STONELYNK CO.</h1>
    <p class="tagline">SCREENERS | CRUSHERS | STACKERS</p>

    <h2 class="person-name">DALE MORVAN</h2>
    <p class="person-title">DIRECTOR</p>

    <div class="rule rule-top"></div>

    <p class="contact contact-online">DALE@STONELYNK.COM<br>WWW.STONELYNK.CA</p>
    <p class="contact contact-office">TEL : 780.555.0142<br>FAX : 780.555.0187</p>
    <p class="contact contact-direct">DIRECT : 780.555.0163</p>

    <div class="rule rule-bottom"></div>

    <p class="contact contact-address">2218 48B AVENUE<br>BRANTMOOR, ALBERTA T0A 1B2</p>

    <svg class="card-bands" width="510" height="292" viewBox="0 0 510 292" aria-hidden="true">
      <polygon points="0,262 330,262 316,292 0,292" fill="var(--brand-green)"/>
      <polygon points="326,268 510,268 510,292 314,292" fill="var(--ink)"/>
    </svg>
  </section>

</body>
</html>
```